Modern Business Card

Modern professional business card with more than just logo and demographic info. Something memorable.

We are a trendy/modern chiropractic group with an emphasis on neurology, hence the minimalist-type brain logo. We want to convey that modern and technical aspect with professionalism and the elite nature of our practice environment.

```html
<!DOCTYPE html>
<html lang="en">
<head>
<meta charset="utf-8">
<title>Keystone Spine Studio – Business Card</title>
<link rel="stylesheet" href="https://fonts.googleapis.com/css2?family=Tinos&family=PT+Sans:wght@400;700&display=swap">
<style>
  :root {
    --brand-blue: #3f78b9;
    --card-white: #f3f3f3;
    --ink: #1c1c1c;
    --backdrop: #5a5a5a;
  }
  * { box-sizing: border-box; margin: 0; padding: 0; }
  html, body { width: 1200px; height: 1021px; overflow: hidden; }
  body {
    background: var(--backdrop);
    display: flex;
    flex-direction: column;
    align-items: center;
    justify-content: center;
    gap: 60px;
  }
  .card {
    position: relative;
    width: 700px;
    height: 400px;
    overflow: hidden;
    box-shadow: 0 8px 24px rgba(0,0,0,.35);
  }
  .card--front {
    background: var(--brand-blue);
    color: #fff;
  }
  .front-wordmark {
    position: absolute;
    right: 70px;
    top: 160px;
    font-family: "Tinos", serif;
    text-transform: uppercase;
    text-align: center;
    line-height: 1;
  }
  .front-wordmark .line-1 { font-size: 52px; letter-spacing: 2px; display: block; }
  .front-wordmark .line-2 { font-size: 30px; letter-spacing: 1px; display: block; margin-top: 4px; }

  .card--back {
    background: linear-gradient(135deg, #f7f7f7, #e9e9e9);
    color: var(--ink);
    font-family: "PT Sans", sans-serif;
  }
  .back-brand {
    position: absolute;
    left: 50px;
    top: 50px;
    display: flex;
    align-items: center;
    gap: 14px;
    font-family: "Tinos", serif;
    text-transform: uppercase;
    line-height: 1;
    color: var(--ink);
  }
  .back-brand .dot {
    width: 38px; height: 38px;
    border-radius: 50%;
    background: var(--brand-blue);
  }
  .back-brand .line-1 { font-size: 34px; letter-spacing: 1px; display: block; }
  .back-brand .line-2 { font-size: 20px; display: block; margin-top: 2px; }

  .contact {
    position: absolute;
    left: 50px;
    top: 140px;
  }
  .contact .name { color: var(--brand-blue); font-weight: 700; font-size: 22px; }
  .contact .role { font-size: 17px; margin-bottom: 16px; }
  .contact .address { font-size: 18px; line-height: 1.25; margin-bottom: 4px; }
  .contact ul { list-style: none; font-size: 18px; line-height: 1.3; }
  .contact li { display: flex; align-items: center; gap: 8px; }
  .contact svg { width: 15px; height: 15px; fill: var(--brand-blue); flex: none; }
  .back-accent {
    position: absolute;
    right: 0;
    top: 0;
    width: 22px;
    height: 100%;
    background: var(--brand-blue);
  }
</style>
</head>
<body>

  <section class="card card--front" aria-label="Card front">
    <div class="front-wordmark">
      <span class="line-1">Keystone</span>
      <span class="line-2">Spine Studio</span>
    </div>
  </section>

  <section class="card card--back" aria-label="Card back">
    <div class="back-brand">
      <span class="dot"></span>
      <div>
        <span class="line-1">Keystone</span>
        <span class="line-2">Spine Studio</span>
      </div>
    </div>

    <div class="contact">
      <p class="name">Dr. Elliot Marsh</p>
      <p class="role">President</p>
      <p class="address">4270 Linden Park Avenue<br>Dayton, Ohio 45402</p>
      <ul>
        <li><svg viewBox="0 0 24 24"><path d="M6.6 10.8a15.1 15.1 0 0 0 6.6 6.6l2.2-2.2c.3-.3.7-.4 1-.2 1.1.4 2.3.6 3.6.6.6 0 1 .4 1 1V20c0 .6-.4 1-1 1A17 17 0 0 1 3 4c0-.6.4-1 1-1h3.5c.6 0 1 .4 1 1 0 1.3.2 2.5.6 3.6.1.3 0 .7-.2 1z"/></svg>555-014-2768</li>
        <li><svg viewBox="0 0 24 24"><path d="M2 5h20v14H2zm2 2v.4l8 5 8-5V7zm0 2.8V17h16V9.8l-8 5z"/></svg>elliot@keystonespine.com</li>
        <li><svg viewBox="0 0 24 24"><path d="M12 2a10 10 0 1 0 0 20 10 10 0 0 0 0-20zm6.9 6h-3a15 15 0 0 0-1.3-3.9A8 8 0 0 1 18.9 8zM12 4c.8 1.2 1.5 2.5 1.9 4h-3.8c.4-1.5 1.1-2.8 1.9-4zM4.3 14a8 8 0 0 1 0-4h3.4a16 16 0 0 0 0 4zm.8 2h3a15 15 0 0 0 1.3 3.9A8 8 0 0 1 5.1 16zm3-8h-3a8 8 0 0 1 4.3-3.9C8.9 5.3 8.4 6.6 8.1 8zM12 20c-.8-1.2-1.5-2.5-1.9-4h3.8c-.4 1.5-1.1 2.8-1.9 4zm2.3-6H9.7a14 14 0 0 1 0-4h4.6a14 14 0 0 1 0 4zm.3 5.9c.6-1.2 1-2.5 1.3-3.9h3a8 8 0 0 1-4.3 3.9zm1.7-5.9a16 16 0 0 0 0-4h3.4a8 8 0 0 1 0 4z"/></svg>www.keystonespine.com</li>
      </ul>
    </div>

    <div class="back-accent"></div>
  </section>

</body>
</html>
```